Consulting/Brand Licensing business needs business card

We need a business card created for our IP company, that also does consulting and brand licensing. We would like this card to be vague, as our other business' are in the cannabis industry and this is a non-cannabis touching entity. Perhaps something that hints vaguely at the industry without alerting or possibly offending the receiver.

Target Market(s)

CEOs/Key Decision Makers/Industry Leaders

Contact Information for Business Card

No address, simply list Seattle, WA. Phone: 206-555-0143. Name: Dario Lindqvist // email: Dario@velmarcoast.com

Colors

Designer to choose colors to be used in the design.

Requirements
Must have
• Logo, Name, Email, Phone number, "Consulting, Licensing and Branding Specialists"
Nice to have
• We would like this to be more professional than playful.

```html
<!DOCTYPE html>
<html lang="en">
<head>
<meta charset="utf-8">
<title>Velmar Coast, Inc — Business Card</title>
<link rel="stylesheet" href="https://fonts.googleapis.com/css2?family=Montserrat:wght@400;600;700&family=Questrial&display=swap">
<style>
  :root {
    --stage: #2b2b2d;
    --brand-orange: #e2512b;
    --brand-orange-light: #ea7453;
    --card-white: #ffffff;
    --card-shade: #ececec;
    --ink: #1f1f1f;
    --ink-soft: #3a3a3a;
    --rule: #555555;
  }
  * { margin: 0; padding: 0; box-sizing: border-box; }
  html, body {
    width: 1200px;
    height: 903px;
    overflow: hidden;
    background: var(--stage);
  }
  .canvas {
    position: relative;
    width: 1200px;
    height: 903px;
  }
  .card {
    position: absolute;
    width: 620px;
    height: 354px;
    border-radius: 22px;
    box-shadow: 0 14px 30px rgba(0,0,0,0.45);
    overflow: hidden;
  }

  /* Back of card */
  .card-back {
    left: 170px;
    top: 70px;
    background: linear-gradient(135deg, var(--brand-orange) 0%, var(--brand-orange) 70%, var(--brand-orange-light) 100%);
  }
  .card-back .back-name {
    position: absolute;
    right: 48px;
    bottom: 56px;
    text-align: right;
    color: var(--card-white);
    font-family: "Montserrat", sans-serif;
    font-weight: 600;
    font-size: 38px;
    line-height: 1;
    letter-spacing: 0.5px;
  }
  .card-back .back-name span {
    display: block;
    font-size: 16px;
    margin-top: 8px;
    letter-spacing: 1px;
  }

  /* Front of card */
  .card-front {
    left: 410px;
    top: 480px;
    background: linear-gradient(160deg, var(--card-white) 0%, var(--card-white) 55%, var(--card-shade) 100%);
    display: flex;
    align-items: center;
    padding: 0 40px;
  }
  .identity {
    width: 290px;
    padding-right: 26px;
  }
  .identity .company {
    color: var(--brand-orange);
    font-family: "Montserrat", sans-serif;
    font-weight: 600;
    font-size: 34px;
    line-height: 1.05;
  }
  .identity .company-legal {
    margin-top: 10px;
    color: var(--ink);
    font-family: "Questrial", sans-serif;
    font-size: 20px;
  }
  .identity .tagline {
    margin-top: 6px;
    color: var(--ink-soft);
    font-family: "Questrial", sans-serif;
    font-size: 15px;
  }
  .divider {
    width: 1px;
    height: 130px;
    background: var(--rule);
  }
  .contact {
    padding-left: 26px;
    font-family: "Questrial", sans-serif;
    color: var(--ink);
  }
  .contact .person {
    font-family: "Montserrat", sans-serif;
    font-size: 20px;
    font-weight: 400;
    letter-spacing: 0.5px;
    margin-bottom: 12px;
  }
  .contact .person strong { font-weight: 700; }
  .contact .line {
    display: flex;
    align-items: center;
    gap: 10px;
    font-size: 16px;
    margin-top: 8px;
  }
  .contact .line svg { flex: none; }
  .contact .location {
    margin-top: 8px;
    padding-left: 28px;
    font-size: 14px;
    color: var(--ink-soft);
  }
</style>
</head>
<body>
<main class="canvas">

  <section class="card card-back" aria-label="Card back">
    <div class="back-name">Velmar Coast<span>Velmar Coast, Inc</span></div>
  </section>

  <section class="card card-front" aria-label="Card front">
    <div class="identity">
      <div class="company">Velmar Coast</div>
      <div class="company-legal">Velmar Coast, Inc</div>
      <div class="tagline">Brand Licensing &amp; Consulting</div>
    </div>
    <div class="divider"></div>
    <div class="contact">
      <div class="person"><strong>DARIO</strong> LINDQVIST</div>
      <div class="line">
        <svg width="18" height="18" viewBox="0 0 18 18" aria-hidden="true">
          <circle cx="9" cy="9" r="9" fill="var(--brand-orange)"/>
          <path d="M6 4.8c.4-.3.9-.2 1.1.2l.8 1.5c.2.4.1.8-.2 1l-.6.5c.4.9 1.1 1.7 2 2.2l.5-.6c.3-.3.7-.4 1-.2l1.5.8c.4.2.5.7.2 1.1l-.6.8c-.4.5-1.1.7-1.7.4C8 11.6 6.4 10 5.5 8c-.3-.6-.1-1.3.4-1.7z" fill="#fff"/>
        </svg>
        206-555-0143
      </div>
      <div class="line">
        <svg width="18" height="18" viewBox="0 0 18 18" aria-hidden="true">
          <circle cx="9" cy="9" r="9" fill="var(--brand-orange)"/>
          <rect x="4.5" y="6" width="9" height="6.5" rx="0.8" fill="#fff"/>
          <path d="M4.8 6.4 9 9.6l4.2-3.2" stroke="var(--brand-orange)" stroke-width="0.9" fill="none"/>
        </svg>
        Dario@velmarcoast.com
      </div>
      <div class="location">Seattle, WA</div>
    </div>
  </section>

</main>
</body>
</html>
```